custom carpentry, woodworking and home repair company needs logo design and business card design

Attention: I apologize but I just received notification from my state that I cannot use the company name that I originally submitted (Beyond The Bench). The new name will be Joinolux We need a company logo and business card design for our new company based in the Hampton Roads area of Virginia. The company name is Joinolux. The final design should give a first impression of true craftsmanship and attention to detail. We would like the card to include the company name, my name Mark Tellman (owner), phone number (757) 348-2615, website (joinolux-example.com) and email address (mark@joinolux-example.com). Everything else is up to your discretion. Thanks, have fun, and good luck.

Industry/Entity Type

Business

Contact Information for Business Card

See project description

Logo Text

see project description

Colors

Designer to choose colors to be used in the design.

```html
<!DOCTYPE html>
<html lang="en">
<head>
<meta charset="utf-8">
<title>Joinolux — Business Card</title>
<link rel="stylesheet" href="https://fonts.googleapis.com/css2?family=Roboto+Slab:wght@300;400;700&display=swap">
<style>
  :root {
    --canvas: #ffffff;
    --ink: #5f6062;
    --accent: #c4ab7f;
    --band: #d4c09e;
    --paper: #ffffff;
    --wood-light: #d9d6d2;
    --wood-mid: #c9c3bb;
    --wood-warm: #d3c6b8;
    --engrave: #aaa49d;
  }
  * { box-sizing: border-box; margin: 0; padding: 0; }
  html, body {
    width: 1026px;
    height: 1200px;
    overflow: hidden;
    background: var(--canvas);
    font-family: "Roboto Slab", Georgia, serif;
  }
  .sheet { position: relative; width: 1026px; height: 1200px; }

  /* Front face */
  .card-front {
    position: absolute;
    left: 65px; top: 66px;
    width: 890px; height: 512px;
    overflow: hidden;
  }
  .wood-surface {
    position: absolute; inset: 0;
    background: linear-gradient(160deg, var(--wood-light) 0%, var(--wood-warm) 35%, var(--wood-mid) 60%, var(--wood-light) 100%);
  }
  .front-name {
    position: absolute;
    left: 0; right: 0; top: 175px;
    text-align: center;
    font-size: 132px;
    font-weight: 400;
    letter-spacing: 6px;
    color: var(--engrave);
  }

  /* Back face */
  .card-back {
    position: absolute;
    left: 69px; top: 625px;
    width: 887px; height: 507px;
    background: var(--paper);
    overflow: hidden;
  }
  .brand-name {
    position: absolute;
    left: 76px; top: 118px;
    font-size: 62px;
    font-weight: 700;
    color: var(--ink);
    line-height: 1;
  }
  .contact {
    position: absolute;
    right: 63px; top: 70px;
    text-align: right;
    color: var(--ink);
  }
  .contact-name { font-size: 27px; font-weight: 300; text-transform: uppercase; line-height: 1.1; }
  .contact-role { font-size: 21px; font-weight: 300; color: var(--accent); line-height: 1.1; }
  .contact-phone { font-size: 25px; font-weight: 300; margin-top: 16px; line-height: 1.3; }
  .contact-email { font-size: 24px; font-weight: 700; line-height: 1.3; }

  .band {
    position: absolute;
    left: 0; right: 0; top: 266px; height: 154px;
    background: var(--band);
    color: #ffffff;
  }
  .appointment-title {
    position: absolute;
    left: 85px; top: 30px;
    font-size: 20px; font-weight: 700;
  }
  .appointment-fields {
    position: absolute;
    left: 85px; top: 86px;
    font-size: 20px; font-weight: 700;
    white-space: nowrap;
  }
  .blank { display: inline-block; width: 132px; border-bottom: 1.5px solid #ffffff; vertical-align: baseline; }
  .website {
    position: absolute;
    right: 63px; top: 68px;
    font-size: 28px; font-weight: 700;
  }
  .services {
    position: absolute;
    left: 0; right: 0; top: 432px;
    text-align: center;
    font-size: 26px; font-weight: 300;
    color: var(--ink);
  }
  .services .highlight { color: var(--accent); }
</style>
</head>
<body>
<main class="sheet">
  <section class="card-front">
    <div class="wood-surface" role="img" aria-label="Pale birch wood grain surface"></div>
    <div class="front-name">Joinolux</div>
  </section>

  <section class="card-back">
    <div class="brand-name">Joinolux</div>

    <div class="contact">
      <div class="contact-name">Mark Tellman</div>
      <div class="contact-role">owner</div>
      <div class="contact-phone">(757) 348-2615</div>
      <div class="contact-email">mark@joinolux-example.com</div>
    </div>

    <div class="band">
      <div class="appointment-title">APPOINTMENT</div>
      <div class="appointment-fields">Date:<span class="blank"></span>Time:<span class="blank"></span></div>
      <div class="website">joinolux-example.com</div>
    </div>

    <div class="services">custom carpentry • <span class="highlight">woodworking</span> • home repairs</div>
  </section>
</main>
</body>
</html>
```